Professional business cards for real estate development company

I need business cards for my new real estate development company. The company, "KORVA" is a real estate development, investment, and advisory firm with a focus on multifamily, office, and mixed-use projects across primary and secondary markets in the Southeast United States.

Style preference is modern

Industry/Entity Type

Real Estate Development

Contact Information for Business Card

The business cards need to include:
Name
Title
Mailing Address
Phone Number
Web Address

Logo is attached. I would like white to be the primary color with incorporation of the company colors: #232D3A and #B5A451

Font styles to use
Other font styles liked:
• Montserrat, Avenir

Requirements
Must have
• Company Logo. No need to include the company name since the name is in the logo.
Should not have
• No line type designs

```html
<!DOCTYPE html>
<html lang="en">
<head>
<meta charset="utf-8">
<title>KORVA Business Cards</title>
<link href="https://fonts.googleapis.com/css2?family=Open+Sans:wght@400;600&family=Roboto:wght@400;700&display=swap" rel="stylesheet">
<style>
  :root {
    --page-bg: #e4e5e9;
    --navy: #242d3a;
    --navy-mark: #4d6584;
    --card-white: #f7f7f8;
    --ink: #262f3c;
    --ink-soft: #4a4f57;
  }
  * { margin: 0; padding: 0; box-sizing: border-box; }
  html, body { width: 1021px; height: 1200px; overflow: hidden; }
  body { background: var(--page-bg); position: relative; font-family: "Roboto", sans-serif; }

  .card { position: absolute; width: 756px; height: 432px; }
  .card--front { left: 134px; top: 120px; background: var(--navy); }
  .card--back  { left: 131px; top: 650px; background: var(--card-white); }

  .wordmark {
    font-family: "Open Sans", sans-serif;
    font-weight: 600;
    letter-spacing: 2px;
    line-height: 1;
  }
  .card--front .wordmark {
    position: absolute; left: 0; right: 0; top: 176px;
    text-align: center; font-size: 80px; color: var(--navy-mark);
  }
  .card--back .wordmark {
    position: absolute; left: 79px; width: 265px; top: 177px;
    text-align: center; font-size: 62px; color: var(--ink);
  }

  .divider {
    position: absolute; left: 374px; top: 110px;
    width: 2px; height: 211px; background: var(--ink);
  }

  .contact { position: absolute; left: 399px; top: 108px; color: var(--ink-soft); }
  .contact__name { font-weight: 700; font-size: 30px; color: var(--ink); line-height: 1.1; }
  .contact__title { font-size: 20px; margin-top: 4px; line-height: 1.2; }
  .contact__address { font-size: 20px; line-height: 28px; margin-top: 14px; }
  .contact__list { list-style: none; margin-top: 10px; font-size: 20px; line-height: 27px; }
  .contact__list li { display: flex; align-items: center; gap: 7px; }
  .contact__list svg { width: 14px; height: 14px; fill: var(--ink); flex: none; }
</style>
</head>
<body>
  <section class="card card--front">
    <div class="wordmark">KORVA</div>
  </section>

  <section class="card card--back">
    <div class="wordmark">KORVA</div>
    <div class="divider"></div>
    <div class="contact">
      <h1 class="contact__name">DANIEL REYES</h1>
      <p class="contact__title">Founder &amp; CEO</p>
      <p class="contact__address">415 Harbor Crest Ave<br>Marlow, GA 30412</p>
      <ul class="contact__list">
        <li>
          <svg viewBox="0 0 24 24" aria-hidden="true"><path d="M6.6 10.8a15.1 15.1 0 0 0 6.6 6.6l2.2-2.2a1 1 0 0 1 1-.25 11.4 11.4 0 0 0 3.6.57 1 1 0 0 1 1 1V20a1 1 0 0 1-1 1A17 17 0 0 1 3 4a1 1 0 0 1 1-1h3.5a1 1 0 0 1 1 1c0 1.25.2 2.45.57 3.57a1 1 0 0 1-.25 1z"/></svg>
          404-555-0182
        </li>
        <li>
          <svg viewBox="0 0 24 24" aria-hidden="true"><path d="M2 5h20v14H2z M2 5l10 8 10-8" fill="none" stroke="#262f3c" stroke-width="2"/><path d="M2 5h20l-10 8z"/></svg>
          hello@korvamail.com
        </li>
        <li>
          <svg viewBox="0 0 24 24" aria-hidden="true"><circle cx="12" cy="12" r="10"/><path d="M2 12h20M12 2c3 3 3 17 0 20M12 2c-3 3-3 17 0 20" fill="none" stroke="#f7f7f8" stroke-width="1.5"/></svg>
          www.korvahomes.com
        </li>
      </ul>
    </div>
  </section>
</body>
</html>
```